Create for us a Shop-Stopper Business Card

We need a standout, first class business card to go along with our new brand strategy. Sleek, Contemporary and fresh.

Colors and theme must sync with our websitewww.pelvorpower.co.uk

We want a business card that has a global brand appeal. TKR Energy is a small UK renewable company that specialises in energy projects in Africa. We want a business card that has the following characteristics: Very short, precise, global, stand out, NOT TOO LOUD but contemporary. The company's colour themes are White, Grey with a hint of green.

Target Market(s)

Business exec, high net worth individuals, investors, commercial leaders, suppliers, government officials

Industry/Entity Type

Solar Energy

Contact Information for Business Card

Logo, Name, Title, Address, web address, email,

Requirements
Must have
• Logo must be sharp
Nice to have
• Adapt fonts from the logo. The large circular side of the logo at the back in a very refreshing way
Should not have
• No solar panel shapes or image.Very little black. If possible avoid black. Its not coming out nice. I think !!!

```html
<!DOCTYPE html>
<html lang="en">
<head>
<meta charset="utf-8">
<title>TKR Energy Business Card</title>
<link rel="stylesheet" href="https://fonts.googleapis.com/css2?family=Questrial&family=Didact+Gothic&display=swap">
<style>
  :root {
    --backdrop: #2e5112;
    --card: #ffffff;
    --brand-green: #6cb02c;
    --deep-green: #2f7a1f;
    --text-grey: #3d3d3d;
    --soft-grey: #d9d9d9;
    --faint-green: #eef2ea;
  }
  * { margin: 0; padding: 0; box-sizing: border-box; }
  html, body { width: 1200px; height: 480px; overflow: hidden; }
  body {
    background: var(--backdrop);
    font-family: "Questrial", "Didact Gothic", sans-serif;
    color: var(--text-grey);
    position: relative;
  }
  .card {
    position: absolute;
    top: 112px;
    height: 258px;
    background: var(--card);
    box-shadow: 4px 6px 10px rgba(0,0,0,0.35);
    overflow: hidden;
  }
  .card-front { left: 107px; width: 492px; }
  .card-back { left: 636px; width: 455px; }

  .brand {
    position: absolute;
    display: flex;
    align-items: center;
  }
  .brand-dot {
    border-radius: 50%;
    background: var(--deep-green);
    flex: none;
  }
  .brand-name {
    color: var(--text-grey);
    font-family: "Questrial", sans-serif;
    letter-spacing: 0.5px;
    white-space: nowrap;
  }
  .card-front .brand { left: 32px; top: 110px; gap: 8px; }
  .card-front .brand-dot { width: 34px; height: 34px; }
  .card-front .brand-name { font-size: 21px; }

  .divider {
    position: absolute;
    left: 227px; top: 66px;
    width: 1px; height: 132px;
    background: var(--soft-grey);
  }
  .contact {
    position: absolute;
    left: 240px; top: 72px;
  }
  .person-name {
    color: var(--brand-green);
    font-size: 18px;
    font-weight: 700;
    letter-spacing: 0.5px;
  }
  .person-title {
    font-size: 11px;
    margin-top: 3px;
    text-transform: uppercase;
  }
  .details { list-style: none; margin-top: 14px; }
  .details li {
    display: flex;
    align-items: center;
    gap: 6px;
    font-size: 12px;
    height: 18px;
  }
  .details svg { width: 9px; height: 9px; fill: var(--brand-green); flex: none; }

  .back-decoration {
    position: absolute;
    right: -40px; top: -10px;
    width: 300px; height: 290px;
    background: radial-gradient(ellipse at 55% 45%, var(--faint-green) 0%, rgba(238,242,234,0.6) 50%, rgba(255,255,255,0) 72%);
  }
  .card-back .brand { left: 78px; top: 94px; gap: 12px; }
  .card-back .brand-dot { width: 58px; height: 58px; }
  .card-back .brand-name { font-size: 34px; }
</style>
</head>
<body>
  <section class="card card-front">
    <div class="brand">
      <span class="brand-dot"></span>
      <span class="brand-name">TKR ENERGY</span>
    </div>
    <div class="divider"></div>
    <div class="contact">
      <h1 class="person-name">ADA MORROW</h1>
      <p class="person-title">Managing Director</p>
      <ul class="details">
        <li>
          <svg viewBox="0 0 10 10"><path d="M5 0a3.5 3.5 0 0 0-3.5 3.5C1.5 6 5 10 5 10s3.5-4 3.5-6.5A3.5 3.5 0 0 0 5 0zm0 5a1.4 1.4 0 1 1 0-2.8A1.4 1.4 0 0 1 5 5z"/></svg>
          14 Harlow Street,LN 20311
        </li>
        <li>
          <svg viewBox="0 0 10 10"><path d="M1 3c0-1 1-2 4-2s4 1 4 2v1H7V3H3v1H1zM2 5h6l1 4H1z"/></svg>
          5550192
        </li>
        <li>
          <svg viewBox="0 0 10 10"><path d="M0 2h10v6H0zM0.8 2.6 5 5.6l4.2-3"/></svg>
          ada@pelvorpower.co.uk
        </li>
        <li>
          <svg viewBox="0 0 10 10"><circle cx="5" cy="5" r="5"/></svg>
          www.pelvorpower.co.uk
        </li>
      </ul>
    </div>
  </section>

  <section class="card card-back">
    <div class="back-decoration" role="img" aria-label="Faint large brand symbol decoration"></div>
    <div class="brand">
      <span class="brand-dot"></span>
      <span class="brand-name">TKR ENERGY</span>
    </div>
  </section>
</body>
</html>
```